Educational non-profit needs an End of the Year Flyer

We need a flyer to mail to our supporters asking for donations to our program. Hillcrest Open Learning Hub runs after school programs for low-income students in Pasadena, CA. This is our end of the year mailing to supporters asking them to finish out the year with their contributions so that we can meet our budget.

Target Market(s)

Donors and supporters of organization

Industry/Entity Type

Non-Profit

Font styles to use
Serif

Colors

Designer to choose colors to be used in the design.

Requirements
Must have
• The project should fit on a 6x9" card, and be printed on front and back. It should show pictures, use the copy I have included, a space for a label address, a stamp, and the return address.
Nice to have
• eye-catching, fun

```html
<!DOCTYPE html>
<html lang="en">
<head>
<meta charset="utf-8">
<title>Hillcrest Open Learning Hub – Year-End Postcard</title>
<link rel="stylesheet" href="https://fonts.googleapis.com/css2?family=Open+Sans:wght@400;600;700;800&display=swap">
<style>
  :root {
    --yellow: #ffe600;
    --gold: #ffc20e;
    --ink: #1b1b1b;
    --white: #ffffff;
    --page: #e4e4e4;
    --photo-a: #b89a80;
    --photo-b: #5c4a44;
  }
  * { box-sizing: border-box; margin: 0; padding: 0; }
  html, body { width: 849px; height: 1200px; overflow: hidden; }
  body {
    background: var(--page);
    font-family: "Open Sans", Arial, sans-serif;
    position: relative;
  }
  .card {
    position: absolute;
    left: 24px;
    width: 802px;
    height: 535px;
    background: var(--white);
    box-shadow: 0 3px 10px rgba(0,0,0,.35);
    overflow: hidden;
  }
  .card--front { top: 53px; }
  .card--back { top: 608px; }
  .card svg.shapes { position: absolute; inset: 0; }

  /* front */
  .brand {
    position: absolute; left: 40px; top: 70px; width: 150px;
    display: flex; flex-direction: column; align-items: center; gap: 10px;
  }
  .brand__dot { width: 58px; height: 58px; border-radius: 50%; background: var(--yellow); border: 3px solid var(--ink); }
  .brand__name { font-size: 14px; font-weight: 700; color: var(--ink); text-align: center; line-height: 1.25; }
  .headline { position: absolute; left: 0; top: 196px; width: 240px; text-align: center; font-weight: 800; line-height: 1.08; }
  .headline .l1 { font-size: 30px; color: var(--ink); }
  .headline .l2 { font-size: 33px; color: var(--gold); }
  .headline .l3 { font-size: 25px; color: var(--ink); margin-top: 4px; }
  .headline .l4 { font-size: 25px; color: var(--gold); margin-top: 3px; }
  .intro {
    position: absolute; left: 19px; top: 354px; width: 210px;
    font-size: 10.6px; line-height: 1.3; color: #222; text-align: justify; text-align-last: center;
  }
  .intro b { font-weight: 700; }

  .contact-bar {
    position: absolute; left: 0; bottom: 0; width: 100%; height: 66px;
    background: var(--ink); color: var(--white);
    display: flex; align-items: center; padding: 0 20px; gap: 40px;
    font-size: 12px; line-height: 1.6;
  }
  .card--back .contact-bar { width: 428px; height: 57px; gap: 10px; padding: 0 18px; }
  .contact-col { display: flex; flex-direction: column; }
  .contact-item { display: flex; align-items: center; gap: 8px; white-space: nowrap; }
  .contact-item svg { width: 12px; height: 12px; flex: none; }
  .contact-item .indent { padding-left: 20px; }
  .dot-mark { width: 11px; height: 11px; border-radius: 50%; background: var(--yellow); flex: none; }

  /* back */
  .budget {
    position: absolute; left: 10px; top: 26px; width: 360px;
    text-align: center; color: var(--yellow); font-size: 26px; line-height: 1.28; font-weight: 400;
  }
  .budget b { font-weight: 700; }
  .appeal { position: absolute; left: 18px; top: 178px; color: var(--ink); font-weight: 800; }
  .appeal__main { font-size: 35px; line-height: 1.1; }
  .appeal__sub { font-size: 18.5px; margin-top: 3px; }
  .giving-note {
    position: absolute; left: 16px; top: 422px; width: 400px;
    text-align: center; font-size: 12px; font-weight: 700; line-height: 1.3; color: var(--ink);
  }
  .stamp-box {
    position: absolute; left: 716px; top: 21px; width: 63px; height: 77px;
    border: 2px solid var(--ink);
  }
</style>
</head>
<body>

<section class="card card--front" aria-label="Postcard front">
  <svg class="shapes" width="802" height="535" viewBox="0 0 802 535">
    <defs>
      <linearGradient id="groupTone" x1="0" y1="0" x2="1" y2="1">
        <stop offset="0" stop-color="#c9b49c"/>
        <stop offset="0.5" stop-color="#8a6a5c"/>
        <stop offset="1" stop-color="#4a3a48"/>
      </linearGradient>
      <linearGradient id="toneA" x1="0" y1="0" x2="1" y2="1">
        <stop offset="0" stop-color="#3a2a28"/>
        <stop offset="1" stop-color="#c88a8a"/>
      </linearGradient>
      <linearGradient id="toneB" x1="0" y1="0" x2="0" y2="1">
        <stop offset="0" stop-color="#7a8a70"/>
        <stop offset="1" stop-color="#c7b7a8"/>
      </linearGradient>
    </defs>
    <path d="M262 0 H300 C300 180 420 330 560 330 C660 330 740 290 802 250 V469 H430 C340 400 268 230 262 0 Z" fill="var(--yellow)"/>
    <path d="M262 0 C268 230 340 400 430 469" fill="none" stroke="var(--ink)" stroke-width="4"/>
    <g role="img" aria-label="Photo of a smiling group of after-school students in a gym">
      <path d="M300 0 H802 V250 C740 290 660 330 560 330 C420 330 300 180 300 0 Z" fill="url(#groupTone)"/>
    </g>
    <path d="M300 0 C300 180 420 330 560 330 C660 330 740 290 802 250" fill="none" stroke="var(--ink)" stroke-width="4"/>
    <circle cx="500" cy="379" r="78" fill="var(--ink)"/>
    <circle cx="500" cy="379" r="72" fill="var(--white)"/>
    <circle cx="500" cy="379" r="68" fill="url(#toneA)" role="img" aria-label="Photo of two young girls smiling together"/>
    <circle cx="694" cy="363" r="90" fill="var(--ink)"/>
    <circle cx="694" cy="363" r="84" fill="var(--white)"/>
    <circle cx="694" cy="363" r="80" fill="url(#toneB)" role="img" aria-label="Photo of kids playing on a playground swing"/>
  </svg>

  <div class="brand">
    <span class="brand__dot"></span>
    <span class="brand__name">Hillcrest Open<br>Learning Hub</span>
  </div>

  <h1 class="headline">
    <div class="l1">WE NEED</div>
    <div class="l2">YOUR HELP</div>
    <div class="l3">TO FINISH OUT</div>
    <div class="l4">2018 STRONG!</div>
  </h1>

  <p class="intro">We have had a wonderful <b>25th year</b> of serving the children and families of Pasadena here at Hillcrest Open Learning Hub with high quality afterschool programs. Hundreds and hundreds of students have been a part of the Bright Start Kids Club family.</p>

  <footer class="contact-bar">
    <div class="contact-col">
      <span class="contact-item"><svg viewBox="0 0 12 12"><path d="M2 1 L4 1 L5 4 L3.6 5 C4.3 6.6 5.4 7.7 7 8.4 L8 7 L11 8 L11 10 C11 10.6 10.6 11 10 11 C5 11 1 7 1 2 C1 1.4 1.4 1 2 1Z" fill="var(--yellow)"/></svg>(626) 555-0148</span>
      <span class="contact-item"><svg viewBox="0 0 12 12"><rect x="0.5" y="2" width="11" height="8" fill="var(--yellow)"/><path d="M0.5 2 L6 6.5 L11.5 2" fill="none" stroke="var(--ink)" stroke-width="1"/></svg>info@hillcrestkids.org</span>
    </div>
    <div class="contact-col">
      <span class="contact-item"><svg viewBox="0 0 12 12"><path d="M6 0.5 C3.8 0.5 2.2 2.2 2.2 4.3 C2.2 7 6 11.5 6 11.5 C6 11.5 9.8 7 9.8 4.3 C9.8 2.2 8.2 0.5 6 0.5Z" fill="var(--yellow)"/><circle cx="6" cy="4.3" r="1.5" fill="var(--ink)"/></svg>Hillcrest Open Learning Hub</span>
      <span class="contact-item"><span class="indent">214 N. Larkspur Ave. Pasadena, CA&nbsp; 91106</span></span>
    </div>
    <div class="contact-col">
      <span class="contact-item"><svg viewBox="0 0 12 12"><g fill="none" stroke="var(--yellow)" stroke-width="1"><circle cx="6" cy="6" r="5"/><ellipse cx="6" cy="6" rx="2.2" ry="5"/><path d="M1 6 H11 M2 3.3 H10 M2 8.7 H10"/></g></svg>www.hillcrestkids.org</span>
      <span class="contact-item"><span class="dot-mark"></span>Hillcrest Open Learning Hub</span>
    </div>
  </footer>
</section>

<section class="card card--back" aria-label="Postcard back">
  <svg class="shapes" width="802" height="535" viewBox="0 0 802 535">
    <defs>
      <linearGradient id="toneC" x1="0" y1="0" x2="1" y2="1">
        <stop offset="0" stop-color="#c9a86a"/>
        <stop offset="1" stop-color="#5a4a3a"/>
      </linearGradient>
      <linearGradient id="toneD" x1="0" y1="0" x2="1" y2="1">
        <stop offset="0" stop-color="#6a5a5a"/>
        <stop offset="1" stop-color="#b08a7a"/>
      </linearGradient>
    </defs>
    <path d="M0 0 H318 C410 30 438 120 434 230 C430 350 440 470 484 535 H0 Z" fill="var(--yellow)"/>
    <path d="M0 0 H318 C380 20 412 80 412 170 H0 Z" fill="var(--ink)"/>
    <path d="M326 0 C418 32 446 124 442 232 C438 352 448 470 492 535" fill="none" stroke="var(--ink)" stroke-width="4"/>
    <circle cx="108" cy="332" r="71" fill="var(--ink)"/>
    <circle cx="108" cy="332" r="66" fill="var(--white)"/>
    <circle cx="108" cy="332" r="62" fill="url(#toneC)" role="img" aria-label="Photo of a student holding up a handwritten letter"/>
    <circle cx="280" cy="332" r="71" fill="var(--ink)"/>
    <circle cx="280" cy="332" r="66" fill="var(--white)"/>
    <circle cx="280" cy="332" r="62" fill="url(#toneD)" role="img" aria-label="Photo of students playing violins"/>
  </svg>

  <h2 class="budget">Our annual budget is<br><b>$275,000</b> &amp; we count on<br><b>$100,000</b> from individual<br>donors</h2>

  <div class="appeal">
    <div class="appeal__main">Will you join with us</div>
    <div class="appeal__sub">for an end of the year contribution?</div>
  </div>

  <p class="giving-note">Remember, you can give online through QuickGive.&nbsp; Just look for the link on our website - www.hillcrestkids.org.<br>Merry Christmas from all of us at HOLH!</p>

  <div class="stamp-box" aria-label="Stamp area"></div>

  <footer class="contact-bar">
    <div class="contact-col">
      <span class="contact-item"><svg viewBox="0 0 12 12"><path d="M2 1 L4 1 L5 4 L3.6 5 C4.3 6.6 5.4 7.7 7 8.4 L8 7 L11 8 L11 10 C11 10.6 10.6 11 10 11 C5 11 1 7 1 2 C1 1.4 1.4 1 2 1Z" fill="var(--yellow)"/></svg>(626) 555-0148</span>
      <span class="contact-item"><svg viewBox="0 0 12 12"><rect x="0.5" y="2" width="11" height="8" fill="var(--yellow)"/><path d="M0.5 2 L6 6.5 L11.5 2" fill="none" stroke="var(--ink)" stroke-width="1"/></svg>info@hillcrestkids.org</span>
    </div>
    <div class="contact-col">
      <span class="contact-item"><svg viewBox="0 0 12 12"><g fill="none" stroke="var(--yellow)" stroke-width="1"><circle cx="6" cy="6" r="5"/><ellipse cx="6" cy="6" rx="2.2" ry="5"/><path d="M1 6 H11 M2 3.3 H10 M2 8.7 H10"/></g></svg>www.hillcrestkids.org</span>
      <span class="contact-item"><span class="dot-mark"></span>Hillcrest Open Learning Hub</span>
    </div>
  </footer>
</section>

</body>
</html>
```